Haunted Attraction Expert Website Design

A complete professional looking web site with 6 total pages.
Includes calendar and email form.
Needs to be word press and mobile user friendly.
Please use photos as labeled for the pages they will be presented on.
Company logo should alternate left and right sides of the page.
See attached layout for directions

Target Market(s)

Professionals, Haunted Attraction Owners/Operators

Industry/Entity Type

It Professional

Coding

Coded - Design and coding required

Number of Pages Required

5+ page

Font styles to use
Sans Serif

Colors

Designer to choose colors to be used in the design.

Requirements
Must have
• Our company logo on each page and photos supplied by me assigned to specific pages.
• Calendar
• Contact US Email Submission Form

```html
<!DOCTYPE html>
<html lang="en">
<head>
<meta charset="utf-8">
<title>FVA – Fright Venue Advisors</title>
<link href="https://fonts.googleapis.com/css2?family=Creepster&family=Oswald:wght@400;700&family=Roboto:ital,wght@0,400;0,700;1,400&family=Rubik+Dirt&display=swap" rel="stylesheet">
<style>
:root{
  --gold:#8b7a2d;
  --gold-bright:#a8902f;
  --gold-dark:#5e511c;
  --cream:#f6eed8;
  --ink:#111;
  --bg:#1b1b1b;
  --bg-soft:#242424;
  --text:#d8d8d8;
  --muted:#aaa;
  --stone:#8c8c8c;
}
*{box-sizing:border-box;margin:0;padding:0}
html,body{width:1200px;height:2459px;overflow:hidden;background:var(--bg)}
body{font-family:'Roboto',sans-serif;color:var(--text);position:relative}
.abs{position:absolute}

/* header */
.site-header{left:0;top:0;width:1200px;height:72px;background:#0d0d0d}
.brand{left:161px;top:12px;font-family:'Oswald',sans-serif;font-weight:700;font-size:38px;color:var(--gold-bright);letter-spacing:2px}
.main-nav{right:163px;top:26px;display:flex;gap:20px;font-family:'Oswald',sans-serif;font-size:15px;color:#eee}
.main-nav a{color:#eee;text-decoration:none}
.main-nav a.active{color:var(--gold-bright)}

/* hero */
.hero{left:0;top:72px;width:1200px;height:472px;background:linear-gradient(180deg,#3a322a 0%,#4d4036 45%,#2b2520 100%)}
.join-box{left:323px;top:341px;width:554px;height:136px;background:rgba(15,15,15,.72)}
.join-title{left:0;top:14px;width:554px;text-align:center;font-family:'Creepster',sans-serif;font-size:44px;color:var(--gold-bright)}
.join-title:before,.join-title:after{content:"";position:absolute;top:30px;width:110px;height:1px;background:var(--gold)}
.join-title:before{left:22px}.join-title:after{right:22px}
.join-input{left:64px;top:80px;width:336px;height:30px;border:1px solid #555;background:#111;color:#888;font-size:11px;padding:8px 10px}
.join-btn{left:410px;top:80px;width:80px;height:30px;background:#cfcfcf;color:#111;font-weight:700;font-size:11px;text-align:center;line-height:30px}

/* welcome */
.welcome{left:0;top:544px;width:1200px;height:787px;background:radial-gradient(ellipse at center,#2a2a2a 0%,#161616 100%)}
.welcome h1{left:0;top:38px;width:1200px;text-align:center;font-family:'Creepster',sans-serif;font-weight:400;font-size:46px;color:#e6e6e6;letter-spacing:2px}
.ornament{left:325px;top:110px;width:550px;height:24px}
.intro{left:240px;top:157px;width:720px;text-align:center;font-size:13.5px;line-height:21px;color:#ddd}
.intro p{margin-bottom:13px}
.service{width:160px;text-align:center;font-size:14px;line-height:18px;color:#ccc}
.service .disc{display:block;width:100px;height:100px;border-radius:50%;background:var(--gold);margin:0 auto 14px}
.tagline{left:0;top:718px;width:1200px;text-align:center;font-size:15px;color:#ccc}

/* gallery */
.gallery-band{left:0;top:1331px;width:1200px;height:88px;background:linear-gradient(180deg,#9a9a9a,#6f6f6f)}
.gallery-band h2{left:0;top:14px;width:1200px;text-align:center;font-family:'Rubik Dirt',sans-serif;font-weight:400;font-size:52px;color:#151515;letter-spacing:2px}
.shot{top:1419px;height:225px}
.arrow-tab{top:1516px;width:18px;height:30px;background:rgba(255,255,255,.35)}

/* calendar + testimonials */
.lower{left:0;top:1644px;width:1200px;height:388px;background:#1e1e1e}
.calendar{left:161px;top:62px;width:267px;border:1px solid var(--gold-dark);border-collapse:collapse;font-size:13px;color:var(--ink)}
.cal-head{height:38px;background:var(--gold);text-align:center;font-weight:700;font-size:15px;color:#111;position:relative}
.cal-nav{position:absolute;top:10px;width:18px;height:18px;border-radius:50%;background:#fff}
.calendar th{height:36px;background:#e9e9e9;font-size:10px;font-weight:400;color:#444;border:1px solid #ccc}
.calendar td{height:36px;width:38px;text-align:center;background:var(--gold);border:1px solid var(--gold-dark)}
.calendar td.off{background:var(--cream);color:#9a7c2c}
.calendar td.today{background:#000;color:#fff;font-weight:700}
.testi-title{left:492px;top:62px;font-family:'Rubik Dirt',sans-serif;font-size:32px;color:#eee}
.testi-rule{left:494px;top:104px;width:44px;height:3px;background:var(--gold)}
.testi-arrows{left:1005px;top:74px;display:flex;gap:2px}
.testi-arrows span{width:14px;height:14px;background:#555}
.avatar{left:492px;top:131px;width:174px;height:174px;border-radius:50%;border:6px solid #888;background:radial-gradient(circle at 50% 40%,#8a7868,#4a4038)}
.quote{left:697px;top:144px;width:345px;font-style:italic;font-size:14px;line-height:20px;color:#ddd}
.author{left:700px;top:282px;font-size:13px;font-weight:700;color:#ddd}

/* contact */
.contact{left:0;top:2032px;width:1200px;height:381px;background:#121212;border-top:3px solid #333}
.contact h2{left:161px;top:42px;font-family:'Rubik Dirt',sans-serif;font-weight:400;font-size:34px;color:#eee}
.contact-rule{left:161px;top:88px;width:50px;height:3px;background:var(--gold)}
.contact-lead{left:161px;top:103px;width:560px;font-size:11.5px;line-height:18px;color:#ccc}
.field{height:28px;border:1px solid #bbb;font-size:11px;color:#ccc;padding:7px 9px}
.submit{left:161px;top:299px;width:144px;height:39px;background:var(--gold);border-radius:4px;color:#111;font-weight:700;font-size:14px;line-height:39px;text-align:center}
.info-title{left:774px;top:154px;font-family:'Oswald',sans-serif;font-weight:700;font-size:21px;color:#ddd}
.info-item{left:774px;display:flex;gap:10px;font-size:12px;color:#ddd;line-height:16px}
.info-item.phone{font-size:17px;font-weight:700}

/* footer */
.site-footer{left:0;top:2413px;width:1200px;height:46px;background:var(--gold)}
.copy{left:161px;top:16px;font-size:11px;color:#111}
.social{left:893px;top:11px;display:flex;gap:8px}
.social span{width:24px;height:24px;border-radius:50%;border:1.5px solid #111}
</style>
</head>
<body>

<header class="site-header abs">
  <div class="brand abs">FVA</div>
  <nav class="main-nav abs">
    <a class="active" href="#">Home</a><a href="#">About</a><a href="#">Consulting</a><a href="#">Expert Witnesses</a><a href="#">Upcoming Events</a><a href="#">Contact Us</a>
  </nav>
</header>

<section class="hero abs" role="img" aria-label="Haunted barn scene with costumed zombie actors">
  <div class="join-box abs">
    <div class="join-title abs">JOIN IN OUR FVA</div>
    <div class="join-input abs">Enter your email...</div>
    <div class="join-btn abs">JOIN NOW!</div>
  </div>
</section>

<section class="welcome abs">
  <h1 class="abs">WELCOME TO FVA</h1>
  <svg class="ornament abs" viewBox="0 0 550 24"><line x1="0" y1="12" x2="255" y2="12" stroke="#8b7a2d"/><line x1="295" y1="12" x2="550" y2="12" stroke="#8b7a2d"/><rect x="266" y="3" width="18" height="18" fill="#a8902f"/></svg>
  <div class="intro abs">
    <p>Fright Venue Advisors FVA provides UBC Unified Building Code, as well as NFSC National Fire Safety Council Code Compliance Safety Training.</p>
    <p>Consulting services that cover all aspects of owning and operating a Haunted Attraction, to include Design, Construction, Staff Training, Safety, Security and Operations.</p>
    <p>Fright Venue Advisors also provides Experienced Witness and Litigation Consulting Services for Safety related legal matters within the Haunted Attraction Industry; cases that involve, fatalities, catastrophic and personal injuries and Haunted Attraction Safety</p>
  </div>
  <div class="service abs" style="left:176px;top:373px"><span class="disc" role="img" aria-label="Investigation icon"></span>Accident / Incident Investigation</div>
  <div class="service abs" style="left:343px;top:373px"><span class="disc" role="img" aria-label="Inspection icon"></span>Attraction Inspections</div>
  <div class="service abs" style="left:510px;top:373px"><span class="disc" role="img" aria-label="Training icon"></span>Crisis Management Training</div>
  <div class="service abs" style="left:685px;top:373px"><span class="disc" role="img" aria-label="Witness icon"></span>Expert Witness</div>
  <div class="service abs" style="left:857px;top:373px"><span class="disc" role="img" aria-label="Haunted house icon"></span>Haunted Attraction Construction</div>
  <div class="service abs" style="left:346px;top:545px"><span class="disc" role="img" aria-label="Scales icon"></span>Litigation Consulting</div>
  <div class="service abs" style="left:515px;top:545px"><span class="disc" role="img" aria-label="Hard hats icon"></span>Safety Training</div>
  <div class="service abs" style="left:689px;top:545px"><span class="disc" role="img" aria-label="Staff board icon"></span>Staff Training</div>
  <div class="tagline abs">For Haunted Houses, Haunted Woods, Corn Mazes and Hay Rides.</div>
</section>

<section>
  <div class="gallery-band abs"><h2 class="abs">PICTURE GALLERY</h2></div>
  <div class="shot abs" style="left:0;width:225px;background:linear-gradient(180deg,#2a3450,#6b5a3e)" role="img" aria-label="Haunted manor facade with award ribbons"></div>
  <div class="shot abs" style="left:225px;width:257px;background:linear-gradient(180deg,#3a2a2a,#7a3a34)" role="img" aria-label="Group of costumed performers"></div>
  <div class="shot abs" style="left:482px;width:260px;background:linear-gradient(180deg,#555,#4a3a34)" role="img" aria-label="Cast posing in front of haunted mansion"></div>
  <div class="shot abs" style="left:742px;width:259px;background:linear-gradient(180deg,#2e2a26,#5a4c40)" role="img" aria-label="Costumed actor at a typewriter"></div>
  <div class="shot abs" style="left:1001px;width:199px;background:linear-gradient(180deg,#cfd3d6,#8a7f78)" role="img" aria-label="Snowy haunted house exterior"></div>
  <div class="arrow-tab abs" style="left:0"></div>
  <div class="arrow-tab abs" style="left:1182px"></div>
</section>

<section class="lower abs">
  <table class="calendar abs">
    <tr><td colspan="7" class="cal-head" style="background:var(--gold);height:38px"><span class="cal-nav" style="left:12px"></span>March 2018<span class="cal-nav" style="right:12px"></span></td></tr>
    <tr><th>MON</th><th>TUE</th><th>WED</th><th>THU</th><th>FRI</th><th>SAT</th><th>SUN</th></tr>
    <tr><td class="off">28</td><td>1</td><td>2</td><td>3</td><td class="today">4</td><td>5</td><td>6</td></tr>
    <tr><td>7</td><td>8</td><td>9</td><td>10</td><td>11</td><td>12</td><td>13</td></tr>
    <tr><td>14</td><td>15</td><td>16</td><td>17</td><td>18</td><td>19</td><td>20</td></tr>
    <tr><td>21</td><td>22</td><td>23</td><td>24</td><td>25</td><td>26</td><td>27</td></tr>
    <tr><td>28</td><td>29</td><td>30</td><td>31</td><td class="off">1</td><td class="off">2</td><td class="off">3</td></tr>
  </table>
  <div class="testi-title abs">TESTIMONIALS</div>
  <div class="testi-rule abs"></div>
  <div class="testi-arrows abs"><span></span><span></span></div>
  <div class="avatar abs" role="img" aria-label="Portrait of client"></div>
  <p class="quote abs">“ Lorem Ipsum is simply dummy text of the printing and has survived not only five centuries, but also the leap into lease of Letraset sheets containing Lorem Ipsum passages, and more recently with desktop publishing software like Aldus PageMaker including versions of text Lorem Ipsum. ”</p>
  <div class="author abs">__Daniel Marsh</div>
</section>

<section class="contact abs">
  <h2 class="abs">CONTACT FORM</h2>
  <div class="contact-rule abs"></div>
  <p class="contact-lead abs">Lorem Ipsum is simply dummy text of the printing and typesetting industry. Lorem Ipsum has been the industry's standard dummy text Lorem Ipsum is simply dummy text.</p>
  <div class="field abs" style="left:161px;top:159px;width:273px">Name</div>
  <div class="field abs" style="left:444px;top:159px;width:274px">Last Name</div>
  <div class="field abs" style="left:161px;top:205px;width:273px">Email</div>
  <div class="field abs" style="left:444px;top:205px;width:274px;height:72px">Massage</div>
  <div class="field abs" style="left:161px;top:249px;width:273px">Phone Number</div>
  <div class="submit abs">SUBMIT NOW ⊙</div>
  <div class="info-title abs">CONTACT INFORMATION:-</div>
  <div class="info-item abs" style="top:196px"><svg width="12" height="16" viewBox="0 0 12 16"><path d="M6 0a6 6 0 0 0-6 6c0 4.5 6 10 6 10s6-5.5 6-10a6 6 0 0 0-6-6z" fill="#ddd"/><circle cx="6" cy="6" r="2.2" fill="#121212"/></svg><span>Lorem Ipsum is simply dummy text<br>the printing and typesetting industry.</span></div>
  <div class="info-item phone abs" style="top:237px"><svg width="14" height="16" viewBox="0 0 14 14"><path d="M3 0l3 3-2 2c1 2 3 4 5 5l2-2 3 3-2 3C6 14 0 8 0 3z" fill="#ddd"/></svg><span>0400 555 019</span></div>
  <div class="info-item abs" style="top:274px"><svg width="14" height="12" viewBox="0 0 14 10"><rect width="14" height="10" fill="#ddd"/><path d="M0 0l7 6 7-6" stroke="#121212" fill="none"/></svg><span>info@fva-example.com</span></div>
</section>

<footer class="site-footer abs">
  <div class="copy abs">© 2018 fva-example.com. All rights reserved.</div>
  <div class="social abs"><span></span><span></span><span></span><span></span><span></span></div>
</footer>

</body>
</html>
```